We need a wesbite for a new company based in London called: 'Belgrove Maids'. We supply the following services in private household: nanny, housekeeper, maternity nurse, driver, carer, companion and cleaner.
We would like to see designs that should communicate good ethics and high standard, quality services and professionalism.

I want a website something like: www.brightnestnursery.co.uk and http://www.tidyhearthstaff.co.uk/ I want the landing page should have at least 3 seconds intervals of changing photos of Asian (only) particularly Filipino (from the Philippines) Nanny with Children, Asian Housekeeper with apron cleaning, a photo of elderly in a wheelchair with the carer and a picture of a happy family with asian nanny in the background cleaning.

```html
<!DOCTYPE html>
<html lang="en">
<head>
<meta charset="utf-8">
<title>Belgrove Maids – Household Services</title>
<link href="https://fonts.googleapis.com/css2?family=Lato:wght@300;400;700&display=swap" rel="stylesheet">
<style>
:root{
  --blue:#1b98d8;
  --blue-dark:#137fb8;
  --ink:#222;
  --text:#666;
  --muted:#8a8a8a;
  --line:#e3e3e3;
  --soft:#f4f4f4;
  --dark:#333437;
  --darker:#242527;
  --white:#fff;
}
*{box-sizing:border-box;margin:0;padding:0}
html,body{width:1200px;height:2839px;overflow:hidden}
body{font-family:'Lato',Arial,sans-serif;color:var(--text);background:var(--white);position:relative}
.abs{position:absolute}
a{color:inherit;text-decoration:none}
.btn{position:absolute;background:var(--blue);color:var(--white);font-size:12px;font-weight:700;display:flex;align-items:center;justify-content:center;gap:6px;box-shadow:3px 4px 0 rgba(0,0,0,.18)}

/* header */
.site-header{position:absolute;left:0;top:0;width:1200px;height:98px;background:var(--white)}
.brand{left:155px;top:18px}
.brand-name{font-size:21px;color:var(--ink);font-weight:400}
.brand-tag{font-size:9px;letter-spacing:3.2px;color:var(--muted);margin-top:2px}
.contact-item{top:22px;display:flex;gap:12px;align-items:center}
.contact-item .ico{width:34px;height:34px;border-radius:50%;border:1px solid var(--line);display:flex;align-items:center;justify-content:center}
.contact-item b{display:block;font-size:12px;color:var(--ink);font-weight:700}
.contact-item span{font-size:11px;color:var(--muted)}
.contact-item .phone{color:var(--blue)}
.main-nav{left:132px;top:80px;width:938px;height:38px;background:var(--white);box-shadow:0 2px 4px rgba(0,0,0,.2);z-index:2}
.main-nav a{position:absolute;top:11px;font-size:11.5px;color:#444}
.main-nav a.active{color:var(--blue);border-bottom:2px solid var(--blue);padding-bottom:8px}
.nav-search{position:absolute;left:782px;top:10px;width:133px;font-size:10px;color:#aaa;display:flex;justify-content:space-between}

/* hero */
.hero{left:0;top:98px;width:1200px;height:402px;background:linear-gradient(90deg,#6b6b6b 0%,#8e8e8e 40%,#b9b9b9 70%,#d6d6d6 100%)}
.hero-title{left:155px;top:117px;font-size:31px;font-weight:300;color:var(--white)}
.hero-title b{font-weight:700}
.hero-copy{left:155px;top:172px;width:470px;font-size:11.5px;line-height:15px;color:var(--white)}
.hero-dots{left:572px;top:358px;display:flex;gap:12px;align-items:center}
.hero-dots i{width:8px;height:8px;border-radius:50%;background:var(--white);display:block}
.hero-dots i.on{width:12px;height:12px;background:transparent;border:2px solid var(--white)}

/* intro */
.intro-title{left:0;top:540px;width:1200px;text-align:center;font-size:21px;line-height:27px;font-weight:700;color:var(--ink)}
.intro-title em{font-style:normal;font-weight:400;color:var(--blue)}
.intro-copy{left:240px;top:616px;width:720px;text-align:center;font-size:11.5px;line-height:17px;color:var(--muted)}

/* services */
.services{left:0;top:786px;width:1200px;height:573px;background:var(--soft)}
.section-title{position:absolute;left:0;width:1200px;text-align:center;font-size:20px;font-weight:700;color:var(--ink)}
.section-title em{font-style:normal;font-weight:400;color:var(--blue)}
.title-rule{position:absolute;left:307px;width:586px;height:1px;background:#d8d8d8}
.title-rule::after{content:"";position:absolute;left:286px;top:-1px;width:12px;height:12px;border-right:1px solid #d8d8d8;border-bottom:1px solid #d8d8d8;transform:rotate(45deg);background:inherit;top:-7px;background:var(--soft)}
.blog .title-rule::after{background:var(--white)}
.svc{position:absolute;width:256px}
.svc h3{font-size:13px;font-weight:400;color:var(--ink);margin-bottom:10px}
.svc p{font-size:11px;line-height:17px;color:var(--muted)}
.svc .more{font-size:10.5px;color:#333;margin-top:3px}
.svc.left{left:160px;text-align:right;padding-right:18px;border-right:1px solid var(--line);height:125px}
.svc.right{left:768px;padding-left:20px;border-left:1px solid var(--line);height:125px}
.svc.active{border:none;border-left:1px solid var(--blue);border-bottom:1px solid var(--blue);background:var(--white);width:276px}
.svc.active h3,.svc.active .more{color:var(--blue)}
.svc-dot{position:absolute;width:9px;height:9px;border-radius:50%;border:2px solid var(--blue);background:var(--soft)}
.svc-sep{position:absolute;height:1px;background:var(--line)}
.svc-photo{left:496px;top:136px;width:208px;height:384px;background:linear-gradient(180deg,#e9e9e9,#cfcfcf 60%,#bdbdbd);border-radius:90px 90px 6px 6px}

/* testimonial */
.reviews{left:0;top:1359px;width:1200px;height:424px;background:linear-gradient(90deg,#3c3d40 0%,#55565a 55%,#6c6d70 100%);overflow:hidden}
.avatar{left:553px;top:114px;width:94px;height:94px;border-radius:50%;border:3px solid var(--white);background:linear-gradient(160deg,#d8d8d8,#9a9a9a)}
.quote{left:230px;top:236px;width:740px;text-align:center;font-size:13px;line-height:21px;font-style:italic;color:var(--white)}
.reviewer{left:0;top:325px;width:1200px;text-align:center;font-size:20px;color:var(--blue)}
.reviewer-role{left:0;top:354px;width:1200px;text-align:center;font-size:11.5px;color:var(--white)}

/* blog */
.post-img{position:absolute;left:155px;width:356px;height:184px}
.date-box{position:absolute;left:536px;width:60px;height:58px;border:2px solid #222;text-align:center;background:var(--white)}
.date-box b{display:block;font-size:20px;color:var(--ink);margin-top:6px;line-height:22px}
.date-box span{font-size:10px;letter-spacing:1px;font-weight:700;color:var(--ink)}
.post-title{position:absolute;left:619px;font-size:13px;color:var(--blue)}
.post-meta{position:absolute;left:619px;font-size:10px;font-style:italic;color:#777}
.post-meta a{color:var(--blue)}
.post-body{position:absolute;left:536px;width:512px;font-size:10.5px;line-height:17px;color:#888}
.read-more{position:absolute;left:536px;font-size:10.5px;color:#333}
.post-sep{position:absolute;left:155px;top:2135px;width:915px;height:1px;background:var(--line)}

/* cta */
.cta{left:0;top:2404px;width:1200px;height:117px;background:linear-gradient(90deg,#1e9bd9,#38a9e0 60%,#2a9fd9)}
.cta h2{position:absolute;left:155px;top:30px;font-size:29px;font-weight:400;color:var(--white)}
.cta p{position:absolute;left:157px;top:68px;font-size:13px;color:var(--white)}
.cta .ghost{position:absolute;left:840px;top:40px;width:203px;height:38px;background:var(--white);color:#333;font-size:13px;display:flex;align-items:center;justify-content:center;gap:8px}

/* footer */
.site-footer{left:0;top:2521px;width:1200px;height:252px;background:var(--dark)}
.f-head{position:absolute;font-size:11px;font-weight:700;color:var(--white);letter-spacing:.3px}
.f-text{position:absolute;font-size:11px;line-height:15px;color:#aaa}
.subscribe{position:absolute;left:155px;top:101px;width:280px;height:28px;border:1px solid #777;font-size:11px;color:#aaa;padding:7px 10px}
.subscribe::after{content:"";position:absolute;right:34px;top:5px;width:1px;height:16px;background:#777}
.social{position:absolute;left:155px;top:188px;display:flex;gap:9px}
.social i{display:block;width:10px;height:10px;border-radius:50%;background:#ccc}
.quick-links{position:absolute;left:536px;top:82px;list-style:none}
.quick-links li{font-size:11px;line-height:17.5px;color:#bbb}
.quick-links li.on{color:var(--blue)}
.f-phone{position:absolute;left:687px;top:155px;font-size:23px;font-weight:300;color:var(--blue);letter-spacing:.5px}
.bottom-bar{left:0;top:2773px;width:1200px;height:66px;background:var(--darker)}
.bottom-bar p{position:absolute;left:155px;top:26px;font-size:11px;color:#ddd}
.bottom-bar p span{color:var(--blue)}
.to-top{position:absolute;left:1006px;top:18px;width:30px;height:30px;border:1px solid var(--blue);transform:rotate(45deg)}
</style>
</head>
<body>

<header class="site-header">
  <div class="abs brand">
    <div class="brand-name">Belgrove Maids</div>
    <div class="brand-tag">Household Services</div>
  </div>
  <div class="abs contact-item" style="left:460px">
    <div class="ico"><svg width="14" height="14" viewBox="0 0 24 24"><path d="M6.6 10.8a15 15 0 0 0 6.6 6.6l2.2-2.2c.3-.3.7-.4 1-.2 1.1.4 2.3.6 3.6.6.6 0 1 .4 1 1V20c0 .6-.4 1-1 1A17 17 0 0 1 3 4c0-.6.4-1 1-1h3.5c.6 0 1 .4 1 1 0 1.3.2 2.5.6 3.6.1.3 0 .7-.2 1z" fill="#555"/></svg></div>
    <div><b>Any Questions at</b><span class="phone">555-555-5555</span></div>
  </div>
  <div class="abs contact-item" style="left:634px">
    <div class="ico"><svg width="14" height="12" viewBox="0 0 24 18"><rect x="1" y="1" width="22" height="16" fill="none" stroke="#555" stroke-width="2"/><path d="M1 1l11 9 11-9" fill="none" stroke="#555" stroke-width="2"/></svg></div>
    <div><b>Send your mail at</b><span>info@belgrovemaids.com</span></div>
  </div>
  <a class="btn" style="left:916px;top:23px;width:127px;height:34px;box-shadow:none">
    <svg width="10" height="10" viewBox="0 0 10 10"><rect x="1" y="1" width="8" height="8" fill="none" stroke="#fff" stroke-width="1.4"/></svg>Get Free Advise</a>
</header>

<nav class="abs main-nav">
  <a class="active" style="left:40px">Home</a>
  <a style="left:120px">About Us</a>
  <a style="left:218px">Our Services ▾</a>
  <a style="left:344px">Testimonial</a>
  <a style="left:456px">Blogs ▾</a>
  <a style="left:545px">Vacancies ▾</a>
  <a style="left:656px">Contact Us</a>
  <div class="nav-search"><span>Search your text...</span>
    <svg width="11" height="11" viewBox="0 0 12 12"><circle cx="5" cy="5" r="3.8" fill="none" stroke="#444" stroke-width="1.6"/><path d="M8 8l3 3" stroke="#444" stroke-width="1.8"/></svg></div>
</nav>

<section class="abs hero" role="img" aria-label="Photo of a housekeeper in an apron vacuuming a bright modern living room">
  <h1 class="abs hero-title">A tradition of <b>quality</b> cleaning</h1>
  <p class="abs hero-copy">Abitant morbi tristique senectus eft netus eft malesuada fames ac turpis egestas enean non tell. Donec pede quam placerat ristique faucibus poserw uete lobortid Lorem ipsum dolor sit amet consectetur.</p>
  <a class="btn" style="left:155px;top:252px;width:129px;height:34px">Schedule Cleaning</a>
  <div class="abs hero-dots"><i></i><i class="on"></i><i></i></div>
</section>

<section>
  <h2 class="abs intro-title">Are you <em>looking for</em> a Housekeeper, Carer, Maternity nurse,<br>Driver, Nanny?</h2>
  <p class="abs intro-copy">We offers the exemplary housekeeping services of experienced British, European, Filipino amongst other Nationalities, as housekeepers, housekeeper/nannies, housekeeper/cooks and mother's helps selected for their experience, reliability and flexibility.</p>
  <a class="btn" style="left:534px;top:702px;width:128px;height:34px">Explore More</a>
</section>

<section class="abs services">
  <h2 class="section-title" style="top:40px">Our Daily &amp; Live In <em>Services include</em></h2>
  <div class="title-rule" style="top:79px"></div>

  <div class="svc left" style="top:136px"><h3>Maternity nurse</h3><p>Morbi fringilla convallis sapien, id pulvinar odio volutpat. Quam temere in vitiis.</p><div class="more">Read more »</div></div>
  <div class="svc left" style="top:270px"><h3>Carer</h3><p>Morbi fringilla convallis sapien, id pulvinar odio volutpat. Quam temere in vitiis.</p><div class="more">Read more »</div></div>
  <div class="svc left" style="top:406px"><h3>Companion and Ceaner</h3><p>Morbi fringilla convallis sapien, id pulvinar odio volutpat. Quam temere in vitiis.</p><div class="more">Read more »</div></div>
  <span class="svc-dot" style="left:425px;top:134px"></span>
  <span class="svc-dot" style="left:425px;top:268px"></span>
  <span class="svc-dot" style="left:425px;top:404px"></span>
  <div class="svc-sep" style="left:160px;top:250px;width:260px"></div>
  <div class="svc-sep" style="left:160px;top:385px;width:260px"></div>

  <div class="abs svc-photo" role="img" aria-label="Photo of a smiling carer supporting an elderly woman with a walking stick"></div>

  <div class="svc right active" style="top:126px;padding-top:10px;height:124px"><h3>Housekeeper</h3><p>Morbi fringilla convallis sapien, id pulvinar odio volutpat. Quam temere in vitiis, legem.</p><div class="more">Read more »</div></div>
  <div class="svc right" style="top:270px"><h3>Nanny</h3><p>Morbi fringilla convallis sapien, id pulvinar odio volutpat. Quam temere in vitiis, legem.</p><div class="more">Read more »</div></div>
  <div class="svc right" style="top:406px"><h3>Driver</h3><p>Morbi fringilla convallis sapien, id pulvinar odio volutpat. Quam temere in vitiis, legem.</p><div class="more">Read more »</div></div>
  <span class="abs" style="left:760px;top:126px;width:16px;height:16px;border-radius:50%;border:2px solid var(--blue);background:var(--white)"></span>
  <span class="svc-dot" style="left:763px;top:268px"></span>
  <span class="svc-dot" style="left:763px;top:404px"></span>
  <div class="svc-sep" style="left:768px;top:385px;width:276px"></div>
</section>

<section class="abs reviews" role="img" aria-label="Photo of a housekeeper making a bed in a bedroom">
  <svg class="abs" style="left:0;top:0" width="1200" height="424" viewBox="0 0 1200 424">
    <polygon points="0,0 150,0 0,110" fill="#1b98d8"/>
    <polygon points="1200,300 1200,424 1030,424" fill="#1b98d8"/>
    <path d="M152 275l-14 16 14 16" fill="none" stroke="#fff" stroke-width="2"/>
    <path d="M1048 275l14 16-14 16" fill="none" stroke="#fff" stroke-width="2"/>
  </svg>
  <h2 class="section-title" style="top:44px;color:#fff">What Clients Say</h2>
  <div class="abs avatar" role="img" aria-label="Client portrait"></div>
  <p class="abs quote">Lorem Ipsum has been the industry's standard dummy text ever since the 1500s, when an unknown printertook a galley of type and scrambled it to make a type specimen book. It has survived not only five centuries but also the leap into electronic ...</p>
  <div class="abs reviewer">Martin Hale</div>
  <div class="abs reviewer-role">- Project Manager at Northgate Labs -</div>
</section>

<section class="blog">
  <h2 class="section-title" style="top:1826px;font-weight:400">Recent blog posts</h2>
  <div class="title-rule" style="top:1865px"></div>

  <div class="post-img" style="top:1920px;background:linear-gradient(135deg,#f3f3f3,#dcdcdc)" role="img" aria-label="Photo of a housekeeper vacuuming beside a white sofa"></div>
  <div class="date-box" style="top:1920px"><b>18</b><span>OCT</span></div>
  <div class="post-title" style="top:1928px">Lorem Ipsum is simply dummy text</div>
  <div class="post-meta" style="top:1953px">By <a>Samir Noor</a> in Development</div>
  <p class="post-body" style="top:1993px">Lorem ipsum dolor sit amet, consetetur sadipscing elitr, sed diam nonumy eirmod tedunt labore et dolore magna aliquyam erat, sed diam voluptua. At vero eos et accusam et justo duo dolores et erebum. Stet clita kasd gubergren, no sea takimata sanctus est Lorem ipsum dolor sit am Lorem ipsum dolor sit amet, consetetur sadipscing elitr, sed diam nonumy eirmod tempor invidulabore et</p>
  <a class="read-more" style="top:2092px">Read more »</a>
  <div class="post-sep"></div>

  <div class="post-img" style="top:2167px;background:linear-gradient(135deg,#ececec,#cfd8dc)" role="img" aria-label="Photo of a housekeeper in a blue apron cleaning a kitchen counter"></div>
  <div class="date-box" style="top:2169px"><b>21</b><span>OCT</span></div>
  <div class="post-title" style="top:2176px">Lorem Ipsum is simply dummy text</div>
  <div class="post-meta" style="top:2201px">By <a>Samir Noor</a> in Development</div>
  <p class="post-body" style="top:2241px">Lorem ipsum dolor sit amet, consetetur sadipscing elitr, sed diam nonumy eirmod tedunt labore et dolore magna aliquyam erat, sed diam voluptua. At vero eos et accusam et justo duo dolores et erebum. Stet clita kasd gubergren, no sea takimata sanctus est Lorem ipsum dolor sit am Lorem ipsum dolor sit amet, consetetur sadipscing elitr, sed diam nonumy eirmod tempor invidulabore et</p>
  <a class="read-more" style="top:2342px">Read more »</a>
</section>

<section class="abs cta">
  <h2>Wanted a Free Consultation?</h2>
  <p>We are always ready to welcome you!</p>
  <a class="ghost">Schedule Cleaning <span>»</span></a>
</section>

<footer class="abs site-footer">
  <div class="f-head" style="left:155px;top:47px">STAY CONNECTED</div>
  <div class="f-text" style="left:155px;top:76px">Top design, tech and startup resources</div>
  <div class="subscribe">Enter Your Email
    <svg class="abs" style="right:10px;top:7px" width="12" height="12" viewBox="0 0 12 12"><path d="M1 6l10-5-3 10-2-4z" fill="none" stroke="#bbb"/></svg></div>
  <div class="f-head" style="left:155px;top:162px">GET SOCIAL</div>
  <div class="social"><i></i><i></i><i></i><i></i><i></i><i></i></div>

  <div class="f-head" style="left:536px;top:47px">QUICK LINKS</div>
  <ul class="quick-links">
    <li class="on">Home</li><li>About Us</li><li>Our Services</li><li>Testimonial</li><li>Blogs</li><li>Vacancies</li><li>Contact Us</li>
  </ul>

  <div class="f-head" style="left:687px;top:47px">KEEP IN TOUCH</div>
  <div class="f-text" style="left:687px;top:78px;color:var(--blue)">Belgrove Maids</div>
  <div class="f-text" style="left:687px;top:93px;width:340px">Contrary to popular belief, Lorem Ipsum is not simply random text.</div>
  <div class="f-head" style="left:687px;top:141px">CONTACT US</div>
  <div class="f-phone">+01 234 - 56789</div>
  <div class="f-text" style="left:687px;top:198px">info@belgrovemaids.com.au</div>
</footer>

<div class="abs bottom-bar">
  <p>© 2016 <span>Belgrove Maids</span>. All rights reserved.</p>
  <div class="to-top"></div>
  <svg class="abs" style="left:1014px;top:28px" width="14" height="9" viewBox="0 0 14 9"><path d="M1 8l6-6 6 6" fill="none" stroke="#1b98d8" stroke-width="1.6"/></svg>
</div>

</body>
</html>
```